"Thank You" card for professional property management agency.

We need to create a DL size "Thank You" card primarily used to thank new clients for their business and referrals.
We are a real estate agency based on Sydney's Northern Beaches. We want the card to feel happy and professional, incorporating our logo.
See our website for details about our business - www.harbourleafrealty.com.au
We have attached our logo in black text and white text as well as some images we have used across our website.
One side must have the ability to hand write a message of thank you on.
I would like this to be a clean and simple design, feel free to use any image supplied, but we are also happy with plain or patterned designs too.

Target Market(s)

Property investors male and female aged 30-60

Industry/Entity Type

Real Estate

Font styles to use
Other font styles liked:
• Please let the designer choose font

Colors

Designer to choose colors to be used in the design.

Requirements
Must have
• DL Size: Full Bleed 213x102mm. Doc size 210x99mm (horizontal)
• Harbour Leaf Realty Logo
• Contact Details:
• info@harbourleafrealty.com.au
• Tel: 0498 217 603
• Level 2, 17 Wattlecombe Rd, Wattlecombe NSW 2187
• "Thank You" somewhere on the card
• Area or side to write message on.
• Design to be provided in editable photoshop PSD file and print ready PDF file
Nice to have
• Sleek professional design that feels "happy or grateful" as it is a thank you card
• Happy to use a plain colour or pattern on one side - it does not have to be an image provided, but feel free to design with either.
Should not have
• should not be too busy, keep it clean and simple.

```html
<!DOCTYPE html>
<html lang="en">
<head>
<meta charset="utf-8">
<title>Harbour Leaf Realty – Thank You Card</title>
<link rel="stylesheet" href="https://fonts.googleapis.com/css2?family=Archivo:wght@800&family=Roboto+Condensed:wght@400;700&display=swap">
<style>
  :root {
    --backdrop: #c4c4c4;
    --card-white: #ffffff;
    --ink: #1b1b1b;
    --teal: #1f7a8c;
    --rule: #bdbdbd;
    --sky-top: #0a4f86;
    --sky-mid: #1a8cc4;
    --sky-low: #4fb4df;
    --shore: #2f5d3a;
    --sea-top: #1a7fb8;
    --sea-deep: #0b4d86;
    --headline: rgba(255,255,255,0.82);
  }
  * { margin: 0; padding: 0; box-sizing: border-box; }
  html, body { width: 1200px; height: 1200px; overflow: hidden; }
  body {
    background: var(--backdrop);
    position: relative;
    font-family: "Roboto Condensed", "Arial Narrow", sans-serif;
  }
  .card { position: absolute; left: 28px; width: 1145px; height: 540px; overflow: hidden; }
  .card--front { top: 38px; }
  .card--back { top: 620px; background: var(--card-white); }

  .harbour-scene {
    position: absolute; inset: 0;
    background: linear-gradient(180deg,
      var(--sky-top) 0%, var(--sky-mid) 38%, var(--sky-low) 56%,
      var(--shore) 63%, var(--sea-top) 68%, var(--sea-deep) 100%);
  }
  .card-frame { position: absolute; left: 28px; top: 26px; width: 1090px; height: 490px; }
  .card--front .card-frame { border: 2px solid rgba(255,255,255,0.9); }
  .card--back .card-frame { border: 2px solid var(--teal); }

  .brand-name {
    position: absolute; white-space: nowrap;
    font-family: "Roboto Condensed", "Arial Narrow", sans-serif;
    font-weight: 700; text-transform: uppercase; letter-spacing: 0.5px;
    display: flex; align-items: center; gap: 10px;
  }
  .brand-name .brand-dot { width: 14px; height: 14px; border-radius: 50%; background: currentColor; }
  .card--front .brand-name { color: var(--card-white); font-size: 38px; left: 0; right: 0; top: 100px; justify-content: center; }
  .card--back .brand-name { color: var(--ink); font-size: 25px; right: 63px; top: 92px; }

  .thank-you { position: absolute; left: 0; top: 0; width: 1145px; height: 540px; }

  .contact { position: absolute; left: 72px; top: 252px; color: var(--ink); font-size: 19px; line-height: 25px; }
  .contact .tel strong { font-size: 23px; font-weight: 700; }

  .message-lines { position: absolute; left: 640px; top: 0; width: 441px; list-style: none; }
  .message-lines li { position: absolute; left: 0; width: 441px; height: 0; border-top: 1px solid var(--rule); }
</style>
</head>
<body>
  <section class="card card--front">
    <div class="harbour-scene" role="img" aria-label="Photograph of a sunny Northern Beaches harbour with moored boats, waterfront houses and a wooded headland under a blue sky"></div>
    <svg class="thank-you" viewBox="0 0 1145 540" aria-label="Thank you">
      <text x="60" y="326" textLength="1052" lengthAdjust="spacingAndGlyphs"
            font-family="Archivo, Arial, sans-serif" font-weight="800" font-size="208"
            fill="var(--headline)">THANK YOU</text>
    </svg>
    <div class="card-frame"></div>
    <div class="brand-name"><span class="brand-dot"></span>Harbour Leaf Realty</div>
  </section>

  <section class="card card--back">
    <div class="card-frame"></div>
    <div class="brand-name"><span class="brand-dot"></span>Harbour Leaf Realty</div>
    <address class="contact" style="font-style:normal">
      <div>info@harbourleafrealty.com.au</div>
      <div class="tel">Tel: <strong>0498 217 603</strong></div>
      <div>Level 2, 17 Wattlecombe Rd,</div>
      <div>Wattlecombe NSW 2187</div>
    </address>
    <ul class="message-lines" aria-label="Lines for a handwritten message">
      <li style="top:288px"></li>
      <li style="top:326px"></li>
      <li style="top:359px"></li>
      <li style="top:397px"></li>
      <li style="top:434px"></li>
      <li style="top:471px"></li>
    </ul>
  </section>
</body>
</html>
```